Business Card for Lawyer

I'm looking for a business card for my new law firm, based in Ontario, Canada. I would prefer single sided. I am partial (but not limited) to white and blue color wise and like things understated. Also, if you can work in the red QK rating symbol from Presworth-Calloway, that would be a plus.

Target Market(s)

Old people - so it should be easy to read.

Industry/Entity Type

Business

Contact Information for Business Card

See the specs in the word document below. Also, see the design for my website. The card should have a similar look to the site.

Requirements
Must have
• Everything listed in the business card specs. I don't mind having the address set off at the bottom of the card on its own line.
Should not have
• 1) Any sort of design that could also be used by a tattoo parlour or a tarot card reader, mystic etc.
• 2) There should not be any photographs of me (or anyone else).

```html
<!DOCTYPE html>
<html lang="en">
<head>
<meta charset="utf-8">
<title>Ashford's Law Firm – Business Card</title>
<link href="https://fonts.googleapis.com/css2?family=Marcellus&family=Quicksand:wght@500&family=Arvo&display=swap" rel="stylesheet">
<style>
  :root {
    --page-bg: #e6e7ea;
    --card-white: #ffffff;
    --brand-blue: #0b4f9f;
    --ink-blue: #1a4fa3;
    --badge-red: #e2242b;
    --on-blue: #ffffff;
  }
  * { box-sizing: border-box; margin: 0; padding: 0; }
  html, body {
    width: 1200px; height: 800px; overflow: hidden;
    background: var(--page-bg);
  }
  .canvas {
    width: 1200px; height: 800px;
    display: flex; align-items: center; justify-content: center;
  }
  .card {
    position: relative;
    width: 1050px; height: 600px;
    background: var(--card-white);
    box-shadow: 0 6px 24px rgba(0,0,0,.18);
    overflow: hidden;
  }
  .identity {
    position: absolute; left: 70px; top: 190px;
    color: var(--ink-blue);
  }
  .identity__name {
    font-family: "Marcellus", serif;
    font-size: 38px; letter-spacing: 2px; font-weight: 400;
  }
  .identity__degrees {
    font-family: "Marcellus", serif;
    font-size: 20px; letter-spacing: 2px; margin: 6px 0 0 14px;
  }
  .identity__roles {
    font-family: "Quicksand", sans-serif; font-weight: 500;
    font-size: 26px; line-height: 1.3; letter-spacing: 1px;
    margin: 22px 0 0 28px;
  }
  .divider {
    position: absolute; left: 575px; top: 130px;
    width: 2px; height: 270px;
    background: linear-gradient(to bottom, rgba(26,79,163,0), var(--ink-blue) 35%, var(--ink-blue) 70%, rgba(26,79,163,0));
  }
  .contact {
    position: absolute; left: 605px; top: 95px;
    list-style: none; color: var(--ink-blue);
    font-family: "Arvo", serif; font-size: 24px; letter-spacing: 1.5px;
  }
  .contact__item { display: flex; align-items: flex-start; margin-bottom: 14px; }
  .contact__icon { width: 34px; height: 30px; flex: none; margin-right: 16px; fill: var(--ink-blue); }
  .contact__address { line-height: 1.25; }
  .contact__postal { font-size: 18px; }
  .band {
    position: absolute; left: 0; bottom: 0;
    width: 100%; height: 175px;
    background: var(--brand-blue);
    color: var(--on-blue);
  }
  .band__firm {
    position: absolute; left: 70px; top: 38px;
    font-family: "Marcellus", serif; font-size: 44px; letter-spacing: 3px; font-weight: 400;
  }
  .band__tagline {
    position: absolute; left: 80px; top: 100px;
    font-family: "Quicksand", sans-serif; font-weight: 500; font-size: 27px; letter-spacing: 1.5px;
  }
  .rating-badge {
    position: absolute; left: 720px; top: 42px;
    width: 260px; height: 64px;
    background: var(--badge-red);
    border-radius: 6px;
  }
</style>
</head>
<body>
<main class="canvas">
  <article class="card">
    <section class="identity">
      <h1 class="identity__name">DANIEL R. ASHFORD</h1>
      <p class="identity__degrees">B.A. &amp; J.D</p>
      <p class="identity__roles">Lawyer, Barrister,<br>Solicitor &amp; Notary Public,<br>Litigation Counsel, Trial Lawyer</p>
    </section>

    <div class="divider"></div>

    <ul class="contact">
      <li class="contact__item">
        <svg class="contact__icon" viewBox="0 0 34 30" aria-hidden="true"><path d="M17 1a10 10 0 0 0-10 10c0 7 10 18 10 18s10-11 10-18A10 10 0 0 0 17 1zm0 14a4 4 0 1 1 0-8 4 4 0 0 1 0 8z"/></svg>
        <span class="contact__address">12 Maple Row East,<br>Ground Floor, Hamilton,<br><span class="contact__postal">ON L8N 4K2</span></span>
      </li>
      <li class="contact__item">
        <svg class="contact__icon" viewBox="0 0 34 30" aria-hidden="true"><path d="M2 10c0-4 6-6 15-6s15 2 15 6v3h-7v-3c-2-1-5-1-8-1s-6 0-8 1v3H2z"/><path d="M6 15h22l3 12H3z"/><circle cx="17" cy="21" r="3.5" fill="#fff"/></svg>
        <span>555-210-xxxx</span>
      </li>
      <li class="contact__item">
        <svg class="contact__icon" viewBox="0 0 34 30" aria-hidden="true"><rect x="10" y="2" width="14" height="10"/><rect x="3" y="11" width="28" height="17" rx="2"/><rect x="8" y="16" width="4" height="3" fill="#fff"/><rect x="14" y="16" width="4" height="3" fill="#fff"/><rect x="8" y="21" width="4" height="3" fill="#fff"/><rect x="14" y="21" width="4" height="3" fill="#fff"/><rect x="21" y="15" width="7" height="10" fill="#fff"/></svg>
        <span>555.318.xxxx</span>
      </li>
      <li class="contact__item">
        <svg class="contact__icon" viewBox="0 0 34 30" aria-hidden="true"><rect x="2" y="6" width="30" height="19"/><path d="M2 6l15 11L32 6" fill="none" stroke="#fff" stroke-width="2"/></svg>
        <span>xxxx@ashfordsfirm.ca</span>
      </li>
      <li class="contact__item">
        <svg class="contact__icon" viewBox="0 0 34 30" aria-hidden="true"><path d="M3 3h28v18H3zm3 3v12h22V6z"/><rect x="14" y="21" width="6" height="4"/><rect x="9" y="25" width="16" height="2.5"/></svg>
        <span>www.ashfordsfirm.ca</span>
      </li>
    </ul>

    <footer class="band">
      <h2 class="band__firm">ASHFORD'S LAW FIRM</h2>
      <p class="band__tagline">Getting the results that matter</p>
      <div class="rating-badge" role="img" aria-label="Peer rating badge from Presworth-Calloway"></div>
    </footer>
  </article>
</main>
</body>
</html>
```